Home delivery Premium Dog Food Company needs Facebook Profile picture cover photo

need artwork for profile pic and cover pic. profile should be 180 X 180 pixels or 540 X 540. cover needs to be 851 X 315 pixels saved as JPG and less than 100 kilobytes. Sugesstions: Integrate profile with cover photo...see 'velmora brisk' on facebook as example. please 'right' align cover photo. Another suggestion is incorporate an offer in cover photo; "Win a years supply of dog treats". please reference the FB specs photo included.

It Company

```html
<!DOCTYPE html>
<html lang="en">
<head>
<meta charset="utf-8">
<title>Win a Years Supply of Dog Treats – Cover</title>
<link rel="stylesheet" href="https://fonts.googleapis.com/css2?family=Lobster&family=Fredoka:wght@500;600&family=Cabin+Sketch:wght@700&display=swap">
<style>
  :root {
    --bg-light: #f3f3f3;
    --bg-mid: #dcdcdc;
    --bg-edge: #bdbdbd;
    --win-orange: #f5a10f;
    --offer-teal: #2ec79a;
    --banner-brown: #3a2f26;
    --banner-text: #ffffff;
    --bubble-fill: #ffffff;
    --bubble-line: #b8b8b8;
    --delicious-gold: #d9b23a;
    --delicious-edge: #8a6a12;
    --paw-tone: rgba(255, 255, 255, 0.45);
    --mascot-light: #f1f1f1;
    --mascot-bone: #e9bf84;
  }
  html, body {
    margin: 0;
    padding: 0;
    width: 1200px;
    height: 444px;
    overflow: hidden;
  }
  .cover {
    position: relative;
    width: 1200px;
    height: 444px;
    overflow: hidden;
    background: radial-gradient(ellipse at 50% 45%, var(--bg-light) 0%, var(--bg-mid) 60%, var(--bg-edge) 100%);
  }
  .paw-trail {
    position: absolute;
    left: 225px;
    top: 190px;
    width: 740px;
    height: 254px;
    background: radial-gradient(ellipse at 40% 55%, var(--paw-tone) 0%, rgba(255,255,255,0) 70%);
  }
  .headline-win {
    position: absolute;
    left: 286px;
    top: 6px;
    margin: 0;
    font-family: "Lobster", cursive;
    font-size: 104px;
    line-height: 1;
    color: var(--win-orange);
    transform: rotate(-4deg);
    text-shadow: 2px 3px 0 rgba(0,0,0,0.12);
  }
  .offer-line {
    position: absolute;
    left: 303px;
    top: 160px;
    margin: 0;
    font-family: "Fredoka", sans-serif;
    font-weight: 600;
    font-size: 47px;
    letter-spacing: 1px;
    line-height: 1;
    color: var(--offer-teal);
    -webkit-text-stroke: 1px #ffffff;
    text-shadow: 0 2px 0 rgba(0,0,0,0.08);
  }
  .prize-banner {
    position: absolute;
    left: 388px;
    top: 226px;
    width: 508px;
    height: 106px;
  }
  .prize-banner svg {
    position: absolute;
    inset: 0;
  }
  .prize-text {
    position: absolute;
    inset: 0;
    margin: 0;
    display: flex;
    align-items: center;
    justify-content: center;
    font-family: "Cabin Sketch", cursive;
    font-weight: 700;
    font-size: 66px;
    letter-spacing: 2px;
    color: var(--banner-text);
    transform: rotate(-2deg);
  }
  .speech-bubble {
    position: absolute;
    left: 744px;
    top: -6px;
    width: 248px;
    height: 96px;
  }
  .speech-bubble svg {
    position: absolute;
    inset: 0;
  }
  .speech-text {
    position: absolute;
    left: 0;
    top: 8px;
    width: 248px;
    margin: 0;
    text-align: center;
    font-family: "Fredoka", sans-serif;
    font-weight: 600;
    font-size: 29px;
    letter-spacing: 1px;
    color: var(--delicious-gold);
    -webkit-text-stroke: 0.8px var(--delicious-edge);
  }
  .mascot {
    position: absolute;
    left: 900px;
    top: 62px;
    width: 250px;
    height: 364px;
    border-radius: 110px 110px 60px 60px;
    background: linear-gradient(180deg, var(--mascot-light) 0%, var(--mascot-light) 62%, var(--mascot-bone) 78%, var(--mascot-bone) 100%);
  }
</style>
</head>
<body>
  <main class="cover">
    <div class="paw-trail" role="img" aria-label="Faint trail of grey paw prints across the background"></div>

    <h1 class="headline-win">Win...</h1>

    <p class="offer-line">A YEARS SUPPLY OF</p>

    <div class="prize-banner">
      <svg width="508" height="106" viewBox="0 0 508 106" aria-hidden="true">
        <path d="M6 24 L500 4 L490 52 L504 98 L14 104 L26 62 Z" fill="var(--banner-brown)"/>
      </svg>
      <p class="prize-text">DOG TREATS</p>
    </div>

    <div class="speech-bubble">
      <svg width="248" height="96" viewBox="0 0 248 96" aria-hidden="true">
        <path d="M20 6 H228 Q244 6 244 22 V58 Q244 74 228 74 H90 L62 94 L68 74 H20 Q4 74 4 58 V22 Q4 6 20 6 Z"
              fill="var(--bubble-fill)" stroke="var(--bubble-line)" stroke-width="2"/>
      </svg>
      <p class="speech-text">DELICIOUS</p>
    </div>

    <div class="mascot" role="img" aria-label="Cartoon white puppy mascot holding a stack of dog biscuit bones"></div>
  </main>
</body>
</html>
```